Visitenkartenvorlage ändern
Zielgruppe
Eventmanagement
Aufgabenstellung
Die beiliegende Visitenkarte wäre das "perfekte" Logo für mich. Da es sich hierbei aber um eine Vorlage eines Online-Druck-Anbieters handelt, darf es leider nur für deren Drucke verwendet werden und nicht für Printwerbung, Homepage etc. Daher sollte es genügend verfremdet werden, so dass ich es verwenden kann.

```html
<!DOCTYPE html>
<html lang="de">
<head>
<meta charset="utf-8">
<title>Neat Affairs – Visitenkarte</title>
<link rel="stylesheet" href="https://fonts.googleapis.com/css2?family=Cinzel:wght@400;500&family=Cormorant+SC:wght@500&family=Pinyon+Script&display=swap">
<style>
  :root {
    --backdrop: #2b2b2c;
    --card: #f1f1f1;
    --card-back: #ececec;
    --pattern: #e2e2e3;
    --ink: #7a7a7a;
    --ink-soft: #8a8a8a;
    --mark: #9a9a9a;
    --band: #c9c9ca;
  }
  * { margin: 0; padding: 0; box-sizing: border-box; }
  html, body { width: 1163px; height: 1200px; overflow: hidden; }
  body { background: var(--backdrop); position: relative; }

  .card {
    position: absolute;
    width: 757px;
    height: 488px;
    background: var(--card);
    color: var(--ink);
    text-align: center;
  }
  .card--front { left: 219px; top: 100px; }
  .card--back  { left: 215px; top: 641px; background: var(--card-back); }

  .wordmark {
    position: absolute; left: 0; right: 0;
    font-family: "Cinzel", serif;
    font-weight: 500;
    font-size: 30px;
    letter-spacing: 3px;
    color: var(--ink);
  }
  .tagline {
    position: absolute; left: 0; right: 0;
    font-family: "Cormorant SC", serif;
    font-weight: 500;
    font-size: 23px;
    letter-spacing: 2px;
    color: var(--ink);
  }
  .web {
    position: absolute; left: 0; right: 0;
    font-family: "Cormorant SC", serif;
    font-weight: 500;
    font-size: 20px;
    letter-spacing: 2px;
    color: var(--ink);
  }
  .mark-dot {
    position: absolute;
    left: 50%;
    border-radius: 50%;
    background: var(--mark);
  }

  .card--front .wordmark { top: 100px; }
  .card--front .mark-dot { top: 180px; width: 120px; height: 120px; margin-left: -60px; }
  .card--front .tagline { top: 356px; }
  .card--front .web { top: 393px; }

  .back-pattern {
    position: absolute; left: 0; right: 0; top: 114px; height: 250px;
    background: linear-gradient(180deg, var(--pattern), var(--card-back));
  }
  .ornament-band {
    position: absolute; left: 14px; right: 14px; top: 110px; height: 10px;
    background: var(--band);
  }
  .card--back .mark-dot { top: 66px; width: 80px; height: 80px; margin-left: -40px; z-index: 1; }
  .card--back .wordmark { top: 163px; }
  .card--back .tagline { top: 218px; }
  .person-name {
    position: absolute; left: 0; right: 0; top: 283px;
    font-family: "Pinyon Script", cursive;
    font-size: 40px;
    color: var(--ink);
  }
  .contact {
    position: absolute; top: 412px;
    font-family: "Cormorant SC", serif;
    font-weight: 500;
    font-size: 22px;
    letter-spacing: 1.5px;
    color: var(--ink-soft);
  }
  .contact--mail { left: 38px; }
  .contact--phone { right: 40px; }
</style>
</head>
<body>

  <section class="card card--front">
    <div class="wordmark">Neat Affairs</div>
    <div class="mark-dot"></div>
    <div class="tagline">Events und mehr</div>
    <div class="web">www.neat-affairs.de</div>
  </section>

  <section class="card card--back">
    <div class="back-pattern" role="img" aria-label="Zartes helles Blumen-Damastmuster"></div>
    <div class="ornament-band" role="img" aria-label="Schmale Zierbordüre aus kleinen Blüten"></div>
    <div class="mark-dot"></div>
    <div class="wordmark">Neat Affairs</div>
    <div class="tagline">Events und mehr</div>
    <div class="person-name">Beluntora Vessin</div>
    <div class="contact contact--mail">info@neat-affairs.de</div>
    <div class="contact contact--phone">+49 170 5550142</div>
  </section>

</body>
</html>
```